Velmora Energy LNG as Marine Fuel Powerpoint Design

Powerpoint template inspired by and using the attached Velmora Energy logo. We are developing LNG as marine fuel facilities and bunkering vessels to supply the fuel to the marine industry. Designs should use the Velmora Energy logo colors and be consistent with our vision of providing environmentally cleaner fuel supply. Our selected logo was 1A in the attached files, as shown on the business card template also attached.

Target Market(s)

Marine Industry (Shipping, container vessels, crude carriers, cargo / transportation vessels, etc.)

Requirements
Must have
• Clean / green energy theme
Compatibility with submitted logo and logo color scheme
Font headers that work well with the logo font
Nice to have
• Marine / Maritime theme
relevance to Gulf Coast Region
Should not have
• Dark colors

```html
<!DOCTYPE html>
<html lang="en">
<head>
<meta charset="utf-8">
<title>Velmora Energy – LNG as Marine Fuel Presentation</title>
<link rel="stylesheet" href="https://fonts.googleapis.com/css2?family=Montserrat:wght@400;700;800&family=Open+Sans:wght@400;600;700&display=swap">
<style>
:root{
  --stage:#e9e5df;
  --slide:#f4f4f4;
  --ink:#1d1d1d;
  --body:#3a3a3a;
  --muted:#777;
  --green:#5bb947;
  --green-light:#8cc63f;
  --teal:#2bbf9a;
  --cyan:#22c4dc;
  --sky:#22aae2;
  --blue:#1a82d0;
  --navy:#1b5faa;
  --gray:#6d6e71;
  --row:#d9d9d9;
  --orange:#f7941d;
}
*{margin:0;padding:0;box-sizing:border-box}
html,body{width:1200px;height:1049px;overflow:hidden;background:var(--stage)}
.canvas{position:relative;width:1200px;height:1049px}
.slide{position:absolute;width:559px;height:316px;background:linear-gradient(180deg,#fff 0%,var(--slide) 60%,#e9e9e9 100%);overflow:hidden;box-shadow:0 2px 6px rgba(0,0,0,.18);font-family:"Open Sans",Arial,sans-serif;color:var(--body)}
.s1{left:31px;top:31px}.s2{left:611px;top:31px}
.s3{left:31px;top:366px}.s4{left:611px;top:366px}
.s5{left:31px;top:704px}.s6{left:611px;top:704px}
.section-name{position:absolute;left:37px;top:30px;font-family:"Montserrat",Arial,sans-serif;font-size:9.5px;color:var(--green);letter-spacing:.3px}
.slide-title{position:absolute;left:37px;top:42px;font-family:"Montserrat",Arial,sans-serif;font-weight:800;font-size:14.5px;color:var(--ink);letter-spacing:.1px}
.brand{position:absolute;right:20px;top:18px;width:70px;text-align:center}
.brand-dot{display:block;width:26px;height:26px;border-radius:50%;background:var(--navy);margin:0 auto 4px}
.brand-name{font-family:"Montserrat",Arial,sans-serif;font-weight:700;font-size:8px;line-height:1.1;color:var(--navy)}
.wave{position:absolute;left:0;bottom:0;width:559px;height:52px}
/* two columns */
.columns{position:absolute;left:37px;top:86px;width:480px;display:flex;gap:24px;font-size:5.6px;line-height:1.3;text-align:justify;color:var(--body)}
.columns div{flex:1;height:200px;overflow:hidden}
/* pyramid */
.pyramid{position:absolute;left:0;top:0}
.floor{position:absolute;font-size:5px;color:var(--muted);line-height:1.25}
.floor b{display:block;font-size:6.5px;color:var(--ink);font-weight:700}
/* circles */
.stat{position:absolute;top:94px;width:110px;text-align:center}
.stat svg{display:block;margin:0 auto}
.stat-title{font-family:"Open Sans",Arial,sans-serif;font-weight:700;font-size:12.5px;color:var(--navy);margin-top:4px}
.stat-text{font-size:6px;line-height:1.3;color:var(--ink);font-weight:600;margin:3px auto 0;width:82px}
/* chart */
.chart{position:absolute;left:0;top:0}
.chart-copy{position:absolute;left:342px;top:104px;width:206px;font-size:7px;line-height:1.3;color:var(--ink);text-align:justify}
.chart-copy p+p{margin-top:8px}
/* table */
.data-table{position:absolute;left:37px;top:90px;width:495px;border-collapse:separate;border-spacing:0;font-size:5.6px}
.data-table th{height:14px;color:#fff;font-family:"Montserrat",Arial,sans-serif;font-weight:700;font-size:6px;text-align:center}
.data-table th.h1{background:linear-gradient(90deg,#174f96,var(--navy));width:209px}
.data-table th.h2{background:var(--sky);width:104px}
.data-table th.h3{background:var(--gray);width:107px}
.data-table th.h4{background:var(--green);width:75px}
.data-table td{height:19px;background:var(--row);text-align:center;color:var(--ink);border-right:1px solid #fff}
.data-table td.lead{text-align:left;padding-left:8px}
.data-table tr.gap td{height:15px;background:transparent;border:0}
/* closing */
.close-brand{position:absolute;left:22px;top:26px;width:92px;text-align:center}
.close-brand .brand-dot{width:44px;height:44px;margin-bottom:6px}
.close-brand .brand-name{font-size:11px}
.thanks{position:absolute;left:22px;top:138px;font-family:"Montserrat",Arial,sans-serif;font-weight:800;font-size:13px;color:var(--ink)}
.contact{position:absolute;left:22px;display:flex;align-items:center;gap:7px;font-size:9px;color:var(--ink);font-weight:600}
.contact svg{flex:none}
.photo{position:absolute;left:123px;top:0;width:436px;height:316px;background:linear-gradient(160deg,#c9dbe8 0%,#e7edf0 30%,#d9c36a 55%,#8a9aa3 80%,#587688 100%)}
</style>
</head>
<body>
<main class="canvas">

<svg width="0" height="0" style="position:absolute">
  <defs>
    <linearGradient id="waveBlue" x1="0" x2="1"><stop offset="0" stop-color="#1a82d0"/><stop offset="1" stop-color="#1b5faa"/></linearGradient>
    <linearGradient id="waveGreen" x1="0" x2="1"><stop offset="0" stop-color="#5bb947"/><stop offset="1" stop-color="#9bd06a"/></linearGradient>
    <linearGradient id="wavePale" x1="0" x2="1"><stop offset="0" stop-color="#cfe8f2"/><stop offset="1" stop-color="#b9dce9"/></linearGradient>
    <symbol id="wave" viewBox="0 0 559 52" preserveAspectRatio="none">
      <path d="M0 26 C120 4 260 4 360 18 C440 28 510 14 559 10 L559 52 L0 52Z" fill="url(#wavePale)"/>
      <path d="M0 34 C110 18 230 18 330 30 C420 40 500 22 559 22 L559 52 L0 52Z" fill="url(#waveGreen)"/>
      <path d="M0 38 C120 28 240 30 340 38 C430 45 500 34 559 32 L559 52 L0 52Z" fill="url(#waveBlue)" opacity=".85"/>
      <path d="M0 44 C140 38 280 42 380 46 C460 49 520 44 559 42 L559 52 L0 52Z" fill="#174f96"/>
    </symbol>
  </defs>
</svg>

<!-- Slide 1 -->
<section class="slide s1">
  <p class="section-name">SECTION NAME HERE</p>
  <h2 class="slide-title">TWO COLOUMN GOES TEXT HERE</h2>
  <div class="brand"><span class="brand-dot"></span><p class="brand-name">Velmora Energy</p></div>
  <div class="columns">
    <div>Lorem ipsum dolor sit amet, consectetur adipiscing elit, sed do eiusmod tempor incididunt ut labore et dolore magna aliqua. Ut enim ad minim veniam, quis nostrud exercitation ullamco laboris nisi ut aliquip ex ea commodo consequat. Duis aute irure dolor in reprehenderit in voluptate velit esse cillum dolore eu fugiat nulla pariatur. Excepteur sint occaecat cupidatat non proident, sunt in culpa qui officia deserunt mollit anim id est laborum. Lorem ipsum dolor sit amet, consectetur adipiscing elit, sed do eiusmod tempor incididunt ut labore et dolore magna aliqua. Ut enim ad minim veniam, quis nostrud exercitation ullamco laboris nisi ut aliquip ex ea commodo consequat. Duis aute irure dolor in reprehenderit in voluptate velit esse cillum dolore eu fugiat nulla pariatur. Excepteur sint occaecat cupidatat non proident, sunt in culpa qui officia deserunt mollit anim id est laborum. Lorem ipsum dolor sit amet, consectetur adipiscing elit, sed do eiusmod tempor incididunt ut labore et dolore magna aliqua. Ut enim ad minim veniam, quis nostrud exercitation ullamco laboris nisi ut aliquip ex ea commodo consequat. Duis aute irure dolor in reprehenderit in voluptate velit esse cillum dolore eu fugiat nulla pariatur. Excepteur sint occaecat cupidatat non proident, sunt in culpa qui officia deserunt mollit anim id est laborum. Lorem ipsum dolor sit amet, consectetur adipiscing elit, sed do eiusmod tempor incididunt ut labore et dolore magna aliqua. Ut enim ad minim veniam, quis nostrud exercitation ullamco laboris nisi ut aliquip ex ea commodo consequat. Duis aute irure dolor in reprehenderit in voluptate velit esse cillum dolore eu fugiat nulla pariatur. Excepteur sint occaecat cupidatat non proident, sunt in culpa qui officia deserunt mollit anim id est laborum.</div>
    <div>Lorem ipsum dolor sit amet, consectetur adipiscing elit, sed do eiusmod tempor incididunt ut labore et dolore magna aliqua. Ut enim ad minim veniam, quis nostrud exercitation ullamco laboris nisi ut aliquip ex ea commodo consequat. Duis aute irure dolor in reprehenderit in voluptate velit esse cillum dolore eu fugiat nulla pariatur. Excepteur sint occaecat cupidatat non proident, sunt in culpa qui officia deserunt mollit anim id est laborum. Lorem ipsum dolor sit amet, consectetur adipiscing elit, sed do eiusmod tempor incididunt ut labore et dolore magna aliqua. Ut enim ad minim veniam, quis nostrud exercitation ullamco laboris nisi ut aliquip ex ea commodo consequat. Duis aute irure dolor in reprehenderit in voluptate velit esse cillum dolore eu fugiat nulla pariatur. Excepteur sint occaecat cupidatat non proident, sunt in culpa qui officia deserunt mollit anim id est laborum. Lorem ipsum dolor sit amet, consectetur adipiscing elit, sed do eiusmod tempor incididunt ut labore et dolore magna aliqua. Ut enim ad minim veniam, quis nostrud exercitation ullamco laboris nisi ut aliquip ex ea commodo consequat. Duis aute irure dolor in reprehenderit in voluptate velit esse cillum dolore eu fugiat nulla pariatur. Excepteur sint occaecat cupidatat non proident, sunt in culpa qui officia deserunt mollit anim id est laborum. Lorem ipsum dolor sit amet, consectetur adipiscing elit, sed do eiusmod tempor incididunt ut labore et dolore magna aliqua. Ut enim ad minim veniam, quis nostrud exercitation ullamco laboris nisi ut aliquip ex ea commodo consequat. Duis aute irure dolor in reprehenderit in voluptate velit esse cillum dolore eu fugiat nulla pariatur. Excepteur sint occaecat cupidatat non proident, sunt in culpa qui officia deserunt mollit anim id est laborum.</div>
  </div>
  <svg class="wave" aria-hidden="true"><use href="#wave"/></svg>
</section>

<!-- Slide 2 -->
<section class="slide s2">
  <p class="section-name">SECTION NAME HERE</p>
  <h2 class="slide-title">PYRAMID CHART SLIDE GOES HERE</h2>
  <div class="brand"><span class="brand-dot"></span><p class="brand-name">Velmora Energy</p></div>
  <svg class="pyramid" width="559" height="316" viewBox="0 0 559 316" font-family="Open Sans, Arial, sans-serif" text-anchor="middle">
    <polygon points="245,77 266,112 224,112" fill="var(--green-light)"/>
    <polygon points="222,115 268,115 288,149 202,149" fill="var(--teal)"/>
    <polygon points="200,152 290,152 310,186 180,186" fill="var(--cyan)"/>
    <polygon points="178,189 312,189 332,223 158,223" fill="var(--sky)"/>
    <polygon points="156,226 334,226 356,263 134,263" fill="var(--blue)"/>
    <text x="245" y="105" font-size="6.5" font-weight="700" fill="#fff">Lorem</text>
    <g font-size="6.5" font-weight="700" fill="#fff">
      <text x="245" y="131">Lorem</text><text x="245" y="168">Lorem</text>
      <text x="245" y="205">Lorem</text><text x="245" y="243">Lorem</text>
    </g>
    <g font-size="5" fill="#fff">
      <text x="245" y="139">Lorem ipsum dolor sit amet.</text>
      <text x="245" y="176">Lorem ipsum dolor sit amet.</text>
      <text x="245" y="213">Lorem ipsum dolor sit amet.</text>
      <text x="245" y="251">Lorem ipsum dolor sit amet.</text>
    </g>
  </svg>
  <p class="floor" style="left:274px;top:94px"><b>Floor 5</b>Lorem ipsum dolor sit amet,<br>consectetur adipiscing elit.</p>
  <p class="floor" style="left:296px;top:129px"><b>Floor 4</b>Lorem ipsum dolor sit amet,<br>consectetur adipiscing elit.</p>
  <p class="floor" style="left:315px;top:162px"><b>Floor 3</b>Lorem ipsum dolor sit amet,<br>consectetur adipiscing elit.</p>
  <p class="floor" style="left:338px;top:199px"><b>Floor 2</b>Lorem ipsum dolor sit amet,<br>consectetur adipiscing elit.</p>
  <p class="floor" style="left:359px;top:232px"><b>Floor 1</b>Lorem ipsum dolor sit amet,<br>consectetur adipiscing elit.</p>
  <svg class="wave" aria-hidden="true"><use href="#wave"/></svg>
</section>

<!-- Slide 3 -->
<section class="slide s3">
  <p class="section-name">SECTION NAME HERE</p>
  <h2 class="slide-title">CIRCLE CHART SLIDE GOES HERE</h2>
  <div class="brand"><span class="brand-dot"></span><p class="brand-name">Velmora Energy</p></div>
  <div class="stat" style="left:56px">
    <svg width="96" height="96" viewBox="0 0 96 96"><circle cx="48" cy="48" r="42" fill="#fff" stroke="var(--navy)" stroke-width="9"/><circle cx="48" cy="48" r="42" fill="none" stroke="var(--green)" stroke-width="9" stroke-dasharray="89.7 264" transform="rotate(-90 48 48)"/><text x="48" y="56" text-anchor="middle" font-family="Open Sans, Arial, sans-serif" font-weight="700" font-size="22" fill="#2a2a2a">34%</text></svg>
    <p class="stat-title">Lorem Ipsum</p>
    <p class="stat-text">Lorem Ipsum is simply dummy text of the printing and typesetting industry. Lorem Ipsum has been the industry's standard dummy text ever since.</p>
  </div>
  <div class="stat" style="left:166px">
    <svg width="96" height="96" viewBox="0 0 96 96"><circle cx="48" cy="48" r="42" fill="#fff" stroke="var(--navy)" stroke-width="9"/><circle cx="48" cy="48" r="42" fill="none" stroke="var(--green)" stroke-width="9" stroke-dasharray="145 264" transform="rotate(-90 48 48)"/><text x="48" y="56" text-anchor="middle" font-family="Open Sans, Arial, sans-serif" font-weight="700" font-size="22" fill="#2a2a2a">55%</text></svg>
    <p class="stat-title">Lorem Ipsum</p>
    <p class="stat-text">Lorem Ipsum is simply dummy text of the printing and typesetting industry. Lorem Ipsum has been the industry's standard dummy text ever since.</p>
  </div>
  <div class="stat" style="left:278px">
    <svg width="96" height="96" viewBox="0 0 96 96"><circle cx="48" cy="48" r="42" fill="#fff" stroke="var(--navy)" stroke-width="9"/><circle cx="48" cy="48" r="42" fill="none" stroke="var(--green)" stroke-width="9" stroke-dasharray="198 264" transform="rotate(-90 48 48)"/><text x="48" y="56" text-anchor="middle" font-family="Open Sans, Arial, sans-serif" font-weight="700" font-size="22" fill="#2a2a2a">75%</text></svg>
    <p class="stat-title">Lorem Ipsum</p>
    <p class="stat-text">Lorem Ipsum is simply dummy text of the printing and typesetting industry. Lorem Ipsum has been the industry's standard dummy text ever since.</p>
  </div>
  <div class="stat" style="left:389px">
    <svg width="96" height="96" viewBox="0 0 96 96"><circle cx="48" cy="48" r="42" fill="#fff" stroke="var(--navy)" stroke-width="9"/><circle cx="48" cy="48" r="42" fill="none" stroke="var(--green)" stroke-width="9" stroke-dasharray="222 264" transform="rotate(-90 48 48)"/><text x="48" y="56" text-anchor="middle" font-family="Open Sans, Arial, sans-serif" font-weight="700" font-size="22" fill="#2a2a2a">84%</text></svg>
    <p class="stat-title">Lorem Ipsum</p>
    <p class="stat-text">Lorem Ipsum is simply dummy text of the printing and typesetting industry. Lorem Ipsum has been the industry's standard dummy text ever since.</p>
  </div>
  <svg class="wave" aria-hidden="true"><use href="#wave"/></svg>
</section>

<!-- Slide 4 -->
<section class="slide s4">
  <p class="section-name">SECTION NAME HERE</p>
  <h2 class="slide-title">TRAINGLE CHART SLIDE GOES HERE</h2>
  <div class="brand"><span class="brand-dot"></span><p class="brand-name">Velmora Energy</p></div>
  <svg class="chart" width="559" height="316" viewBox="0 0 559 316" font-family="Open Sans, Arial, sans-serif" font-size="6" fill="#333">
    <g stroke="#777" stroke-width="1">
      <line x1="53" y1="87" x2="53" y2="236"/><line x1="53" y1="236" x2="308" y2="236"/>
      <line x1="50" y1="87" x2="53" y2="87"/><line x1="50" y1="117" x2="53" y2="117"/><line x1="50" y1="147" x2="53" y2="147"/><line x1="50" y1="177" x2="53" y2="177"/><line x1="50" y1="207" x2="53" y2="207"/>
      <line x1="70" y1="236" x2="70" y2="240"/><line x1="114" y1="236" x2="114" y2="240"/><line x1="158" y1="236" x2="158" y2="240"/><line x1="202" y1="236" x2="202" y2="240"/><line x1="246" y1="236" x2="246" y2="240"/><line x1="290" y1="236" x2="290" y2="240"/>
    </g>
    <g text-anchor="end"><text x="46" y="89">150</text><text x="46" y="119">120</text><text x="46" y="149">90</text><text x="46" y="179">60</text><text x="46" y="209">30</text><text x="46" y="238">0</text></g>
    <polygon points="66,226 85,141 104,226" fill="#9ea3a8"/>
    <polygon points="104,226 123,121 142,226" fill="#c98a45"/>
    <polygon points="143,226 160,179 177,226" fill="#9fc5c9"/>
    <polygon points="178,226 197,139 216,226" fill="#6bb8dc"/>
    <polygon points="216,226 237,106 258,226" fill="#5b7c93"/>
    <polygon points="258,226 280,82 302,226" fill="#3e6a8a"/>
    <g text-anchor="middle" font-weight="600"><text x="70" y="250">2016</text><text x="114" y="250">2017</text><text x="158" y="250">2018</text><text x="202" y="250">2019</text><text x="246" y="250">2020</text><text x="290" y="250">2021</text></g>
  </svg>
  <div class="chart-copy">
    <p>Lorem Ipsum is simply dummy text of the printing and typesetting industry. Lorem Ipsum has been the industry's standard dummy text ever since the 1500s, when an unknown printer took a galley of type and scrambled it to make a type specimen book.</p>
    <p>Contrary to popular belief, Lorem Ipsum is not simply random text. It has roots in a piece of classical Latin literature from 45 BC, making it over 2000 years old. Harold Winslet, a Latin professor at Ashford Ridge College.</p>
  </div>
  <svg class="wave" aria-hidden="true"><use href="#wave"/></svg>
</section>

<!-- Slide 5 -->
<section class="slide s5">
  <p class="section-name">SECTION NAME HERE</p>
  <h2 class="slide-title">TABLE SLIDE GOES HERE</h2>
  <div class="brand"><span class="brand-dot"></span><p class="brand-name">Velmora Energy</p></div>
  <table class="data-table">
    <thead><tr><th class="h1">HEADING 1</th><th class="h2">HEADING 2</th><th class="h3">HEADING 3</th><th class="h4">HEADING 4</th></tr></thead>
    <tbody>
      <tr class="gap"><td colspan="4"></td></tr>
      <tr><td class="lead">Lorem ipsum dolor sit amet, consectetur adipiscing elit, sed do eiusmod</td><td>XXX</td><td>Lorem ipsum</td><td>XXX</td></tr>
      <tr class="gap"><td colspan="4"></td></tr>
      <tr><td class="lead">Lorem ipsum dolor sit amet, consectetur adipiscing elit, sed do eiusmod</td><td>XXX</td><td>Lorem ipsum</td><td>XXX</td></tr>
      <tr class="gap"><td colspan="4"></td></tr>
      <tr><td class="lead">Lorem ipsum dolor sit amet, consectetur adipiscing elit, sed do eiusmod</td><td>XXX</td><td>Lorem ipsum</td><td>XXX</td></tr>
      <tr class="gap"><td colspan="4"></td></tr>
      <tr><td class="lead">Lorem ipsum dolor sit amet, consectetur adipiscing elit, sed do eiusmod</td><td>XXX</td><td>Lorem ipsum</td><td>XXX</td></tr>
      <tr class="gap"><td colspan="4"></td></tr>
      <tr><td class="lead">Lorem ipsum dolor sit amet, consectetur adipiscing elit, sed do eiusmod</td><td>XXX</td><td>Lorem ipsum</td><td>XXX</td></tr>
    </tbody>
  </table>
  <svg class="wave" aria-hidden="true"><use href="#wave"/></svg>
</section>

<!-- Slide 6 -->
<section class="slide s6">
  <div class="photo" role="img" aria-label="Photo of a worker in orange coveralls walking along a yellow-railed walkway on an offshore LNG platform over the sea"></div>
  <div class="close-brand"><span class="brand-dot"></span><p class="brand-name">Velmora Energy</p></div>
  <p class="thanks">THANK YOU!</p>
  <p class="contact" style="top:172px">
    <svg width="14" height="14" viewBox="0 0 14 14"><circle cx="7" cy="7" r="7" fill="#1b75bb"/><path d="M4.6 3.6l1.4 1.6-.7.9c.5 1 1.2 1.8 2.3 2.3l.9-.7 1.6 1.4-.9 1.1C6.6 10 4 7.4 3.5 4.5z" fill="#fff"/></svg>
    555-0142-7780</p>
  <p class="contact" style="top:199px">
    <svg width="14" height="14" viewBox="0 0 14 14"><circle cx="7" cy="7" r="7" fill="var(--orange)"/><rect x="3.5" y="4.5" width="7" height="5" fill="#fff"/><path d="M3.5 4.7L7 7.3l3.5-2.6" fill="none" stroke="var(--orange)" stroke-width=".8"/></svg>
    hello@velmora.example</p>
  <p class="contact" style="top:226px">
    <svg width="14" height="14" viewBox="0 0 14 14"><circle cx="7" cy="7" r="7" fill="var(--green)"/><circle cx="7" cy="7" r="3.6" fill="none" stroke="#fff" stroke-width=".9"/><path d="M3.4 7h7.2M7 3.4c-1.6 2-1.6 5.2 0 7.2M7 3.4c1.6 2 1.6 5.2 0 7.2" fill="none" stroke="#fff" stroke-width=".7"/></svg>
    www.velmora.example</p>
  <svg class="wave" aria-hidden="true"><use href="#wave"/></svg>
</section>

</main>
</body>
</html>
```